Awesome Web Design Project

must have a link to mingleton of the homepage preferably a scrolling view of our mingleton page!

We are an exciting new electrical company with a strong focus on energy efficiency and offering the latest technologies.

The design should allow easy navigation, there shouldn't be too many menus, It should look clean and sleek, Colours to consider could be green, silver/chrome, black,

The site should convey technology, efficiency and simplicity

Must be viewable on all devices, pc's, tablets, phones ie Responsive
Updates

Logo and some pics uploaded!

Industry/Entity Type

Electrical

Requirements
Must have
• must include the following pages,
about us
our services
gallery
contact us
Connect with us
Nice to have
• Would be great if the website design used a user friendly cms,
Should not have
• too many links, menus, clutter it should be clean and easy to navigate

```html
<!DOCTYPE html>
<html lang="en">
<head>
<meta charset="utf-8">
<title>Volton Electrical</title>
<link rel="stylesheet" href="https://fonts.googleapis.com/css2?family=Arimo:ital,wght@0,400;0,700;1,400;1,700&family=Varela+Round&display=swap">
<style>
:root{
  --teal:#2d5d66;
  --teal-dark:#1f4a52;
  --lime:#d4dc1c;
  --ink:#333;
  --text:#555;
  --page:#f3f3f3;
  --footer:#676767;
  --footer-bar:#4f4f4f;
  --line:#d6d6d6;
}
*{box-sizing:border-box;margin:0;padding:0}
html,body{width:1052px;height:1200px;overflow:hidden}
body{font-family:"Arimo",Arial,sans-serif;background:var(--page);color:var(--text);position:relative}
.header{position:absolute;left:0;top:0;width:1052px;height:123px;background:linear-gradient(#fff 0,#fff 60%,#ececec 100%)}
.brand{position:absolute;left:124px;top:24px;display:flex;align-items:center;gap:10px;font-family:"Varela Round",sans-serif;font-size:34px;color:var(--teal);letter-spacing:3px}
.brand-mark{width:40px;height:40px;background:var(--lime);border-radius:4px}
.call{position:absolute;left:723px;top:27px;display:flex;align-items:center;gap:10px}
.call-icon{width:40px;height:40px;border-radius:4px;background:linear-gradient(#dfe24a,#a9ae12);display:flex;align-items:center;justify-content:center;box-shadow:0 1px 2px rgba(0,0,0,.3)}
.call-label{font-size:12px;font-style:italic;color:var(--teal)}
.call-number{font-size:25px;font-weight:700;font-style:italic;color:#333;line-height:1}
.nav{position:absolute;left:124px;top:93px;width:804px;height:30px;background:linear-gradient(#f4f4f4,#d4d4d4);display:flex;font-size:12.5px}
.nav a{color:#222;text-decoration:none;display:flex;align-items:center;justify-content:center;border-right:1px solid #bbb;height:22px;margin-top:4px}
.nav a.active{background:linear-gradient(#4a7a84,#2a5860);color:#fff;font-weight:700;height:30px;margin-top:0;border:none}
.band{position:absolute;left:0;top:123px;width:1052px;height:313px;background:linear-gradient(#5a8890,#1f4f57)}
.slider{position:absolute;left:123px;top:129px;width:806px;height:329px;background:#fff;border-radius:5px;padding:8px}
.slide{width:789px;height:280px;background:linear-gradient(90deg,#c9a456 0%,#e2c98f 35%,#9a5a32 65%,#6a3620 100%)}
.caption{height:33px;background:#202020;display:flex;align-items:center;justify-content:space-between;padding:0 10px;font-family:"Varela Round",sans-serif;color:#fff;font-size:16px}
.dots{display:flex;gap:8px}
.dots i{width:12px;height:12px;border-radius:50%;background:#8a8a8a}
.dots i.on{background:var(--lime)}
.slider-shadow{position:absolute;left:150px;top:458px;width:750px;height:36px;background:radial-gradient(ellipse at 50% 0,rgba(0,0,0,.35),rgba(0,0,0,0) 60%)}
h2{font-family:"Varela Round",sans-serif;font-weight:400;color:var(--teal);display:flex;align-items:center;gap:12px}
h2 .mark{width:22px;height:22px;background:var(--lime);border-radius:3px;display:inline-block}
.about{position:absolute;left:128px;top:490px;width:533px}
.about h2{font-size:22px;padding-bottom:8px;border-bottom:1px dotted #bbb}
.about p{font-size:10px;line-height:17.5px;margin-top:9px;padding-left:3px}
.btn{display:inline-block;background:linear-gradient(#3f6e77,#1f4a52);color:#fff;font-size:10px;font-weight:700;padding:5px 9px;border-radius:3px}
.about .btn{position:absolute;right:2px;top:178px}
.contacts{position:absolute;left:695px;top:490px;width:213px}
.contacts h2{font-size:22px;padding-bottom:8px;border-bottom:1px dotted #bbb}
.field{height:20px;border:1px solid #aaa;border-radius:3px;background:#f4f4f4;font-size:10px;color:#222;padding:3px 10px;margin:7px 0 0 1px;width:211px}
.field.msg{height:43px}
.contacts .btn{position:absolute;right:6px;top:183px}
.divider{position:absolute;left:150px;top:708px;width:700px;height:2px;background:linear-gradient(90deg,transparent,#d0d0d0,transparent)}
.card{position:absolute;top:740px;width:243px;height:222px;background:#e4e4e4;border-radius:8px;padding:5px}
.card-inner{background:#ececec;border:1px solid #fff;border-radius:6px;height:100%;padding:8px 6px;position:relative}
.card h3{font-family:"Varela Round",sans-serif;font-weight:400;color:var(--teal);font-size:19px;display:flex;align-items:center;gap:10px;margin-left:2px}
.card h3 .mark{width:20px;height:20px;background:var(--lime);border-radius:3px}
.card .pic{width:222px;height:100px;margin:8px 0 0 0;border-radius:3px}
.card p{font-size:11px;line-height:16.5px;margin-top:10px;letter-spacing:.2px}
.card .more{position:absolute;right:12px;bottom:9px;font-size:10px;font-weight:700;color:var(--teal);text-decoration:underline}
.card-shadow{position:absolute;top:962px;width:230px;height:10px;background:radial-gradient(ellipse at 50% 0,rgba(0,0,0,.3),rgba(0,0,0,0) 65%)}
.footer{position:absolute;left:0;top:1023px;width:1052px;height:148px;background:var(--footer);color:#fff}
.footer h4{font-size:12.5px;font-weight:700;padding-bottom:7px;border-bottom:1px solid #888}
.fcol{position:absolute;top:16px}
.links{display:grid;grid-template-columns:103px 103px;column-gap:27px;margin-top:4px}
.links span{font-size:10.5px;border-bottom:1px dotted #888;padding:7px 0 6px 10px;position:relative}
.links span::before{content:"›";position:absolute;left:0;top:6px;font-size:10px}
.quote{font-size:10.5px;font-style:italic;line-height:17px;margin-top:9px;padding-left:3px}
.quote-by{text-align:right;font-size:11px;font-weight:700;margin-top:2px;padding-right:12px}
.addr{background:#575757;border-radius:6px;width:208px;padding:10px 14px;margin-top:6px;font-size:10.5px;line-height:12px}
.addr div{display:flex;gap:12px;margin:3px 0 5px}
.bottom{position:absolute;left:0;top:1171px;width:1052px;height:29px;background:var(--footer-bar);color:#fff;font-size:10.5px;display:flex;align-items:center;padding:0 124px;justify-content:space-between}
.social{display:flex;gap:8px;font-size:10px;font-weight:700}
.social span{display:flex;align-items:center;gap:4px}
.social i{width:10px;height:10px;background:#4a8ac4;display:inline-block}
</style>
</head>
<body>
<header class="header">
  <div class="brand"><span class="brand-mark"></span>VOLTON ELECTRICAL</div>
  <div class="call">
    <div class="call-icon"><svg width="22" height="22" viewBox="0 0 24 24"><path fill="#fff" d="M6.6 10.8a15 15 0 0 0 6.6 6.6l2.2-2.2c.3-.3.7-.4 1-.2 1.1.4 2.3.6 3.6.6.6 0 1 .4 1 1V20c0 .6-.4 1-1 1A17 17 0 0 1 3 4c0-.6.4-1 1-1h3.5c.6 0 1 .4 1 1 0 1.3.2 2.5.6 3.6.1.3 0 .7-.2 1z"/></svg></div>
    <div><div class="call-label">Call Us</div><div class="call-number">987 654 3210</div></div>
  </div>
  <nav class="nav">
    <a class="active" style="width:90px">Home</a>
    <a style="width:99px">About Us</a>
    <a style="width:123px">Our Services</a>
    <a style="width:88px">Gallery</a>
    <a style="width:114px">Contact Us</a>
    <a style="width:135px;border:none">Connect with us</a>
  </nav>
</header>

<div class="band"></div>
<section class="slider">
  <div class="slide" role="img" aria-label="Warmly lit hotel bedroom with bedside lamps and a timber headboard"></div>
  <div class="caption"><span>If It needs Electricity We Can Provide a Solution</span><span class="dots"><i class="on"></i><i></i><i></i></span></div>
</section>
<div class="slider-shadow"></div>

<section class="about">
  <h2><span class="mark"></span>About Volton Electrical</h2>
  <p>Lorem ipsum dolor sit amet, consectetuer adipiscing elit, sed diam nonummy nibh euismod tincidunt ut laoreet dolore magna aliquam erat volutpat. Ut wisi enim ad minim veniam, quis nostrud exerci tation ullamcorper suscipit lobortis nisl ut aliquip ex ea commodo consequat. Duis autem vel eum iriure dolor in hendrerit in vulputate velit esse molestie consequat, vel illum dolore eu feugiat nulla facilisis at vero eros et accumsan et iusto odio dignissim qui blandit amet praesent luptatum zzril delenit augue duis dolore te feugait nulla facilisi. lenit augue duis dolore te feugait nul</p>
  <p>Duis autem vel eum iriure dolor in hendrerit in vulputate velit esse molestie consequat, vel illum dolore eu feugiat nulla facilisis at vero eros et accumsan et iusto odio dignissim qui blandit amet praesent luptatum zzril delenit augue duis dolore te feugait nulla facilisi. lenit augue duis dolore te feugait nul</p>
  <span class="btn">Read More</span>
</section>

<section class="contacts">
  <h2><span class="mark"></span>Quick Contacts</h2>
  <div class="field">Name</div>
  <div class="field">Email</div>
  <div class="field">Phone</div>
  <div class="field msg">Message</div>
  <span class="btn">Read More</span>
</section>

<div class="divider"></div>

<article class="card" style="left:127px"><div class="card-inner">
  <h3><span class="mark"></span>Residential</h3>
  <div class="pic" role="img" aria-label="Home interior with pendant lights and warm wall lighting" style="background:linear-gradient(90deg,#5b4a22,#c9a45a 50%,#7a6530)"></div>
  <p>Lorem ipsum dolor sit amet, consectetuer delenit augue duis dolore te feugait nulla.</p>
  <span class="more">Read More »</span>
</div></article>
<div class="card-shadow" style="left:134px"></div>

<article class="card" style="left:404px"><div class="card-inner">
  <h3><span class="mark"></span>Commercial</h3>
  <div class="pic" role="img" aria-label="Bright commercial warehouse space with ceiling fluorescent lights" style="background:linear-gradient(#d8dde0,#a9b2b6)"></div>
  <p>Lorem ipsum dolor sit amet, consectetuer delenit augue duis dolore te feugait nulla.</p>
  <span class="more">Read More »</span>
</div></article>
<div class="card-shadow" style="left:411px"></div>

<article class="card" style="left:682px"><div class="card-inner">
  <h3><span class="mark"></span>Strata Management</h3>
  <div class="pic" role="img" aria-label="Building corridor with shelving and ceiling light strips" style="background:linear-gradient(90deg,#3c3028,#8a8a8c 40%,#c8c8cc)"></div>
  <p>Lorem ipsum dolor sit amet, consectetuer delenit augue duis dolore te feugait nulla.</p>
  <span class="more">Read More »</span>
</div></article>
<div class="card-shadow" style="left:689px"></div>

<footer class="footer">
  <div class="fcol" style="left:123px;width:243px">
    <h4>QUICK LINKS</h4>
    <div class="links">
      <span>Home</span><span>Gallery</span>
      <span>About Us</span><span>Contact Us</span>
      <span>Our Services</span><span>Connect with us</span>
    </div>
  </div>
  <div class="fcol" style="left:420px;width:218px">
    <h4>TESTIMONIALS</h4>
    <p class="quote">"Lorem ipsum dolor sit amet, consectetuer adipiscing elit, sed diam nonummy nibh euismod tincidunt ut laoreet dolore magna aliquam"</p>
    <p class="quote-by">Mr xyz, state</p>
  </div>
  <div class="fcol" style="left:699px;width:220px;top:10px">
    <h4 style="font-weight:400">CONTACT US</h4>
    <div class="addr">
      <div><svg width="10" height="13" viewBox="0 0 10 14"><path fill="#fff" d="M5 0a5 5 0 0 0-5 5c0 4 5 9 5 9s5-5 5-9a5 5 0 0 0-5-5zm0 7a2 2 0 1 1 0-4 2 2 0 0 1 0 4z"/></svg><span>1234A Street Name, City Name<br>Zip Code1234</span></div>
      <div><svg width="11" height="11" viewBox="0 0 24 24"><path fill="#fff" d="M6.6 10.8a15 15 0 0 0 6.6 6.6l2.2-2.2c.3-.3.7-.4 1-.2 1.1.4 2.3.6 3.6.6.6 0 1 .4 1 1V20c0 .6-.4 1-1 1A17 17 0 0 1 3 4c0-.6.4-1 1-1h3.5c.6 0 1 .4 1 1 0 1.3.2 2.5.6 3.6.1.3 0 .7-.2 1z"/></svg><span>1300 12 34 56</span></div>
      <div><svg width="11" height="9" viewBox="0 0 12 9"><rect width="12" height="9" fill="#fff"/><path d="M0 0l6 5 6-5" stroke="#575757" fill="none"/></svg><span>info@voltonelec.example</span></div>
    </div>
  </div>
</footer>
<div class="bottom">
  <span>© 2013 Voltonelectrical. All Rights Reserved.</span>
  <span class="social"><span><i></i>mingleton</span><span><i></i>Linkwell</span><span><i></i>Chirpr</span></span>
</div>
</body>
</html>
```